B2B flyer solution for charging infrastructures (One-Pager Din A4, double-sided)

We need a professional design for our flyer in format Din A4/both sides.
Attached you will find the content for the flyer, but we are looking for a modern, professional design.

Some background/context information:
- the product is about a solution for charging and billing of charging infrastructures (for electric cars) in companies
- target group: companies, esp. facility managers, fleet managers, controlling, CTO, CEO
- should be printed and available online
- our website (and most of our current design work): https://vornix-tech.de

In the files you will find:
- photos of reference implementations of our solution (should be included in the flyer)
- stock photos (we are using the one you will find in the current flyer on our presentations, maybe you can use it too to keep some corporate identity.
- our logo
- the current flyer as PDF and as PowerPoint
- a sample presentation we also need for customer communication

It would be nice if the design will align with the existing design work, but bring fresh aspects and will be up-to-date and professional.

Target Market(s)

B2B, companies, fleet managers, facility managers, CTO, CIO

Industry/Entity Type

Enterprises, Charging Solutions for Electric Vehicles

Requirements
Nice to have
• Bright, light design, clean, readable

```html
<!DOCTYPE html>
<html lang="de">
<head>
<meta charset="utf-8">
<title>vornix Professional – Flyer</title>
<link rel="stylesheet" href="https://fonts.googleapis.com/css2?family=Montserrat:wght@400;500;600;700;800&display=swap">
<style>
:root{
  --bg:#ededf0;
  --purple:#7b2fb5;
  --purple-deep:#5a1e9a;
  --violet:#9b3fd0;
  --magenta:#c61fb0;
  --pink:#e24bc8;
  --lavender:#f1e8fb;
  --ink:#2a1d3a;
  --white:#ffffff;
}
*{box-sizing:border-box;margin:0;padding:0}
html,body{width:1200px;height:854px;overflow:hidden;background:var(--bg);font-family:"Montserrat",sans-serif;color:var(--ink)}
.sheet{position:absolute;top:31px;width:560px;height:792px;background:var(--white);overflow:hidden;box-shadow:0 6px 18px rgba(0,0,0,.12)}
.sheet--front{left:30px}
.sheet--back{left:610px}
.layer{position:absolute;inset:0;width:560px;height:792px}
.abs{position:absolute}
.brand-name{font-weight:600;font-size:17px;letter-spacing:-.2px}
.brand-dot{display:inline-block;width:10px;height:10px;border-radius:50%;background:currentColor;margin-right:6px;vertical-align:1px}
.title{font-weight:800;font-size:37px;line-height:40px;color:var(--white);letter-spacing:-.3px}
.lead{color:var(--white);font-size:11.5px;line-height:16px;font-weight:500}
.diamond{position:absolute;transform:rotate(45deg);border-radius:34px;overflow:hidden}
.diamond .photo{position:absolute;inset:-30%;transform:rotate(-45deg)}
.h-accent{color:var(--magenta);font-weight:700;font-size:18px;line-height:21px}
.list{list-style:none}
.list li{position:relative;font-size:11.5px;line-height:15px;font-weight:500;white-space:nowrap}
.bullet{position:absolute;width:14px;height:14px;border-radius:50%;border:2px solid var(--magenta);background:var(--white)}
.bullet::after{content:"";position:absolute;inset:3px;border-radius:50%;background:var(--magenta)}
.bullet--light{border-color:var(--white);background:transparent}
.bullet--light::after{background:var(--white)}
/* front */
.benefits{right:40px;top:464px;text-align:right}
.benefits li{padding-right:24px;margin-bottom:7px}
.benefits .bullet{right:0;top:1px}
.services{left:25px;top:616px}
.services li{padding-left:26px;margin-bottom:10px;font-size:11.5px;line-height:15.5px}
.services .bullet{left:2px;top:1px}
.contact-box{right:22px;top:628px;width:200px;text-align:right;color:var(--white)}
.contact-box h3{font-size:12px;font-weight:500;line-height:14px}
.contact-box p{font-size:9px;line-height:11.5px;margin-top:14px}
.contact-line{color:var(--white);font-weight:600;display:flex;align-items:center;gap:6px;white-space:nowrap}
/* back */
.service-list{right:22px;top:150px;text-align:right}
.service-list li{padding-right:20px;font-size:9.5px;line-height:11px;margin-bottom:6px;font-weight:600}
.service-list .bullet{right:0;top:-1px;width:13px;height:13px}
.bars .bar{position:absolute;right:20px;height:20px;background:linear-gradient(90deg,rgba(226,75,200,0) 0%,var(--pink) 30%,var(--magenta) 100%);color:var(--white);font-size:9.5px;font-weight:700;line-height:20px;text-align:right;padding-right:28px;border-radius:2px 10px 10px 2px;white-space:nowrap}
.bar::after{content:"";position:absolute;right:6px;top:4px;width:12px;height:12px;border-radius:3px;background:rgba(255,255,255,.85)}
.integration-list{left:20px;top:605px}
.integration-list li{padding-left:28px;font-size:9.5px;line-height:12px;font-weight:700;margin-bottom:9px}
.integration-list .bullet{left:0;top:0;width:13px;height:13px}
.owner-list{right:22px;top:640px;text-align:right;color:var(--white)}
.owner-list li{padding-right:26px;font-size:9.5px;line-height:12px;font-weight:700;margin-bottom:9px}
.owner-list .bullet{right:0;top:1px;width:15px;height:15px}
.footer-back{left:20px;top:768px;right:20px;display:flex;align-items:center;color:var(--white);font-size:11px;font-weight:600;white-space:nowrap}
</style>
</head>
<body>

<!-- FRONT PAGE -->
<section class="sheet sheet--front">
  <svg class="layer" viewBox="0 0 560 792" aria-hidden="true">
    <defs>
      <linearGradient id="frontWash" x1="0" y1="0" x2="1" y2="1">
        <stop offset="0" stop-color="#f6effd"/><stop offset="1" stop-color="#efe3fb"/>
      </linearGradient>
      <linearGradient id="frontPurple" x1="0" y1="0" x2="1" y2="1">
        <stop offset="0" stop-color="#6a27ad"/><stop offset="1" stop-color="#a13ad0"/>
      </linearGradient>
      <linearGradient id="frontBottom" x1="0" y1="0" x2="1" y2="1">
        <stop offset="0" stop-color="#8a35c8"/><stop offset="1" stop-color="#c42bb6"/>
      </linearGradient>
    </defs>
    <rect width="560" height="792" fill="url(#frontWash)"/>
    <path d="M0 540 Q180 470 330 560 T560 520 V792 H0 Z" fill="#e9d8fa" opacity=".7"/>
    <path d="M0 0 H205 L345 130 Q362 148 345 165 L0 505 Z" fill="url(#frontPurple)"/>
    <path d="M0 505 L0 640 Q60 600 120 640 L40 560 Z" fill="#8d34c6" opacity=".5"/>
    <path d="M278 792 L352 640 Q368 608 410 608 H560 V792 Z" fill="url(#frontBottom)"/>
    <path d="M296 756 H560 V792 H278 Z" fill="#6d28b0" opacity=".45"/>
  </svg>
  <svg class="layer" viewBox="0 0 560 792" role="img" aria-label="Foto: Elektroauto wird an einer Ladestation mit blau leuchtendem Stecker geladen">
    <defs>
      <linearGradient id="carPhoto" x1="0" y1="0" x2="1" y2="1">
        <stop offset="0" stop-color="#3b56d6"/><stop offset=".45" stop-color="#dfe7f6"/><stop offset="1" stop-color="#8fb0e6"/>
      </linearGradient>
    </defs>
    <path d="M215 0 H560 V300 L455 405 Q430 430 405 405 L300 300 Q360 230 345 165 Q362 148 345 130 Z" fill="url(#carPhoto)"/>
  </svg>
  <div class="abs brand-name" style="right:24px;top:44px;color:var(--ink)"><span class="brand-dot" style="color:var(--magenta)"></span>vornix-tech.de</div>
  <h1 class="abs title" style="left:25px;top:72px">vornix<br>Professional</h1>
  <p class="abs lead" style="left:26px;top:157px;width:290px">die maßgeschneiderte B2B-Abrechnungslösung für Elektromobilität</p>
  <p class="abs lead" style="left:26px;top:198px;width:270px">Lade-Infrastruktur-Abrechnungslösungen für Unternehmen, damit Lade-Infrastruktur Erträge statt Kosten produziert.</p>

  <div class="diamond" style="left:38px;top:311px;width:190px;height:190px;border:10px solid var(--magenta)">
    <div class="photo" role="img" aria-label="Foto: Ladestecker an einer Ladesäule vor unscharfen Lichtern" style="background:radial-gradient(circle at 60% 40%,#c9d3ea 0%,#5c6a8e 55%,#2b3352 100%)"></div>
  </div>

  <h2 class="abs h-accent" style="right:36px;top:402px;text-align:right">Mit vornix<br>Professional profitieren:</h2>
  <ul class="abs list benefits">
    <li><span class="bullet"></span>Mit vornix Professional profitieren</li>
    <li><span class="bullet"></span>Effizienter Verwaltung von Lade-Infrastruktur</li>
    <li><span class="bullet"></span>Umfassende Full-Service-Betreuung</li>
    <li><span class="bullet"></span>Nahtloser Integration in Ihre<br>kaufmännischen Prozesse</li>
    <li><span class="bullet"></span>Vielseitigen Abrechnungsmöglichkeiten</li>
  </ul>

  <h2 class="abs h-accent" style="left:25px;top:584px">Leistungen:</h2>
  <ul class="abs list services">
    <li><span class="bullet"></span>Vielseitige Abrechnungsmöglichkeiten<br>für Fuhrpark, Mitarbeiter, Partnerunternehmen,<br>Mieter, Kunden und andere.</li>
    <li><span class="bullet"></span>Full-Service-Betreuung (Monitoring,<br>Abrechnung, Benutzerbetreuung)</li>
    <li><span class="bullet"></span>Integration in ihre Unternehmensabläufe</li>
    <li><span class="bullet"></span>Berücksichtigung von Eigentümer/<br>Mieter-Konstellationen</li>
  </ul>

  <div class="abs contact-box">
    <h3>Kontaktieren<br>Sie uns</h3>
    <p>Erfahren Sie mehr über vornix und wie wir Ihre Abrechnungsanforderungen erfüllen können. Kontaktieren Sie uns für eine kostenlose Beratung:</p>
  </div>
  <div class="abs contact-line" style="right:22px;top:740px;font-size:14px">
    <svg width="12" height="12" viewBox="0 0 24 24" aria-hidden="true"><path d="M6.6 10.8a15 15 0 0 0 6.6 6.6l2.2-2.2a1 1 0 0 1 1-.3 11 11 0 0 0 3.6.6 1 1 0 0 1 1 1V20a1 1 0 0 1-1 1A17 17 0 0 1 3 4a1 1 0 0 1 1-1h3.5a1 1 0 0 1 1 1 11 11 0 0 0 .6 3.6 1 1 0 0 1-.3 1z" fill="#fff"/></svg>
    +49 (0) 3040 118 275
  </div>
  <div class="abs contact-line" style="right:22px;top:768px;font-size:11px">
    <svg width="12" height="9" viewBox="0 0 24 18" aria-hidden="true"><rect x="1" y="1" width="22" height="16" rx="2" fill="none" stroke="#fff" stroke-width="2"/><path d="M1 2l11 8 11-8" fill="none" stroke="#fff" stroke-width="2"/></svg>
    info@vornix-tech.de
    <svg width="11" height="11" viewBox="0 0 24 24" aria-hidden="true" style="margin-left:6px"><circle cx="12" cy="12" r="10" fill="none" stroke="#fff" stroke-width="2"/><path d="M2 12h20M12 2c3 3 3 17 0 20M12 2c-3 3-3 17 0 20" fill="none" stroke="#fff" stroke-width="1.6"/></svg>
    www.vornix-tech.de
  </div>
</section>

<!-- BACK PAGE -->
<section class="sheet sheet--back">
  <svg class="layer" viewBox="0 0 560 792" aria-hidden="true">
    <defs>
      <linearGradient id="backWash" x1="0" y1="0" x2="1" y2="1">
        <stop offset="0" stop-color="#fbeefa"/><stop offset="1" stop-color="#f3e6fb"/>
      </linearGradient>
      <linearGradient id="backPurple" x1="0" y1="0" x2="0" y2="1">
        <stop offset="0" stop-color="#7f2fbc"/><stop offset="1" stop-color="#9a3ccc"/>
      </linearGradient>
      <linearGradient id="backBlock" x1="0" y1="0" x2="1" y2="1">
        <stop offset="0" stop-color="#8a36c9"/><stop offset="1" stop-color="#c52bb5"/>
      </linearGradient>
    </defs>
    <rect width="560" height="792" fill="url(#backWash)"/>
    <path d="M0 0 H295 V230 Q295 300 260 330 L200 385 Q120 420 0 430 Z" fill="url(#backPurple)"/>
    <path d="M295 792 V500 Q300 465 340 455 L500 440 Q560 440 560 470 V792 Z" fill="url(#backBlock)"/>
    <path d="M0 760 H560 V792 H0 Z" fill="#a331c4"/>
    <path d="M0 760 H300 V792 H0 Z" fill="#c22bb6"/>
  </svg>
  <div class="abs brand-name" style="left:30px;top:40px;color:var(--white)"><span class="brand-dot"></span>vornix-tech.de</div>
  <h1 class="abs title" style="left:20px;top:92px">vornix<br>Professional</h1>
  <p class="abs lead" style="left:21px;top:178px;width:260px">die maßgeschneiderte B2B-Abrechnungslösung für Elektromobilität</p>

  <div class="diamond" style="left:64px;top:256px;width:206px;height:206px;border:10px solid var(--white)">
    <div class="photo" role="img" aria-label="Foto: Ladestecker wird in ein Elektroauto gesteckt, warmes Licht" style="background:radial-gradient(circle at 45% 55%,#f08a5d 0%,#b9c3d6 30%,#8795b3 70%,#56637f 100%)"></div>
  </div>

  <h2 class="abs h-accent" style="right:20px;top:42px;text-align:right;font-size:16px;line-height:19px">Full-Service-Betreuung für<br>sorgenfreies Management</h2>
  <p class="abs" style="right:20px;top:88px;width:200px;text-align:right;font-size:9.5px;line-height:13px;color:var(--purple)">vornix übernimmt auf Wunsch alle organisatorischen Belange bei der Verwaltung Ihrer Lade-Infrastruktur, einschließlich:</p>
  <ul class="abs list service-list">
    <li><span class="bullet"></span>Monitoring</li>
    <li><span class="bullet"></span>Support</li>
    <li><span class="bullet"></span>User-Onboarding und -Support</li>
    <li><span class="bullet"></span>Handling von Zugangskarten</li>
    <li><span class="bullet"></span>Integration von<br>firmeninternen Zugangstoken</li>
  </ul>

  <h2 class="abs h-accent" style="right:20px;top:271px;text-align:right;font-size:16px;line-height:19px">Verrechnung von<br>Ladevorgängen für</h2>
  <div class="bars">
    <div class="bar" style="top:316px;width:245px">Fuhrpark, Dienstwagen</div>
    <div class="bar" style="top:342px;width:220px">Mitarbeiter Privatfahrzeuge</div>
    <div class="bar" style="top:368px;width:235px">Kunden und Gäste</div>
    <div class="bar" style="top:394px;width:250px">Vermieter, Eigentümer</div>
  </div>

  <h2 class="abs h-accent" style="left:20px;top:530px;font-size:16px;line-height:19px">Perfekte Integration in<br>kaufmännische Prozesse</h2>
  <p class="abs" style="left:20px;top:572px;width:265px;font-size:9.5px;line-height:13px;color:var(--purple)">vornix fügt sich nahtlos in die kaufmännischen Strukturen moderner Unternehmen ein und bietet:</p>
  <ul class="abs list integration-list">
    <li><span class="bullet"></span>Erweitertes Reporting</li>
    <li><span class="bullet"></span>Aufschlüsselung und Tarifierung<br>nach Nutzergruppe</li>
    <li><span class="bullet"></span>Unterstützung unternehmensinterner<br>Abrechnung und Verrechnung und/oder<br>Zahlungseinzug durch vornix</li>
    <li><span class="bullet"></span>Schnittstellen zu Buchhaltung<br>und Lohnbuchhaltung</li>
    <li><span class="bullet"></span>Bedarfsgerechte Anpassbarkeit</li>
  </ul>

  <h2 class="abs" style="right:20px;top:520px;text-align:right;color:var(--white);font-weight:700;font-size:15.5px;line-height:17px">Besonderer Aspekt:<br>Eigentümer-Mieter<br>-Konstellationen</h2>
  <p class="abs" style="right:20px;top:580px;width:210px;text-align:right;color:var(--white);font-size:9.5px;line-height:13px">Häufige Situation: Der Mieter eines Objektes benötigt Lade-Infrastruktur, der Eigentümer/Verwalter möchte nicht zusätzlich belastet werden.</p>
  <ul class="abs list owner-list">
    <li><span class="bullet bullet--light"></span>Unterschiedliche Betreibermodelle<br>für verschiedene Situationen<br>(Langzeit-Mieter vs. Kurzzeit-Mieter)</li>
    <li><span class="bullet bullet--light"></span>Kauf-, Miet- und Leasing-Optionen</li>
    <li><span class="bullet bullet--light"></span>Kostenneutral für Eigentümer/<br>Verwalter durch geeignete<br>Abrechnungsmodelle</li>
  </ul>

  <div class="abs footer-back">
    <svg width="15" height="11" viewBox="0 0 24 18" aria-hidden="true"><rect x="1" y="1" width="22" height="16" rx="2" fill="none" stroke="#fff" stroke-width="2"/><path d="M1 2l11 8 11-8" fill="none" stroke="#fff" stroke-width="2"/></svg>
    <span style="margin:0 16px 0 6px">info@vornix-tech.de</span>
    <svg width="13" height="13" viewBox="0 0 24 24" aria-hidden="true"><circle cx="12" cy="12" r="10" fill="none" stroke="#fff" stroke-width="2"/><path d="M2 12h20M12 2c3 3 3 17 0 20M12 2c-3 3-3 17 0 20" fill="none" stroke="#fff" stroke-width="1.6"/></svg>
    <span style="margin-left:6px">www.vornix-tech.de</span>
    <span style="margin-left:auto;font-size:9.5px">+49 (0) 3040 118 275</span>
    <svg width="11" height="11" viewBox="0 0 24 24" aria-hidden="true" style="margin-left:8px"><path d="M6.6 10.8a15 15 0 0 0 6.6 6.6l2.2-2.2a1 1 0 0 1 1-.3 11 11 0 0 0 3.6.6 1 1 0 0 1 1 1V20a1 1 0 0 1-1 1A17 17 0 0 1 3 4a1 1 0 0 1 1-1h3.5a1 1 0 0 1 1 1 11 11 0 0 0 .6 3.6 1 1 0 0 1-.3 1z" fill="#fff"/></svg>
  </div>
</section>

</body>
</html>
```